Corrow Family Farm fresh honey jar label

I need a label for jars of honey harvested at our farm. These are for gifts and personal use. We are looking to incorporate our farm brand into the label. We would like the design to take the existing brand and add some element like bees, honey, flowers, or hives to indicate the contents. We want the design to feel homemade and authentic without feeling cheap or hoaky

Requirements
Must have
• The label must be made to fit a 1" x2" rectangular label. The label must include the attached family brand. The label must include the text "Corrow Family Farms" "Pinebrook, USA" "Farm Fresh Honey". The label will be printed on off-white paper
Nice to have
• It would be nice to have illustrations of bees or flowers around the logo or hives or honeycombs. The label should have a vintage feel
Should not have
• The label should not feel overly cartoonish or hoaky

```html
<!DOCTYPE html>
<html lang="en">
<head>
<meta charset="utf-8">
<title>Corrow Family Farms – Farm Fresh Honey Label</title>
<link href="https://fonts.googleapis.com/css2?family=Tenor+Sans&display=swap" rel="stylesheet">
<style>
  :root {
    --page: #ffffff;
    --paper: #f6efe3;
    --ink: #1b1918;
    --bee-tone: #b9b2a6;
  }
  html, body {
    margin: 0;
    padding: 0;
    width: 1200px;
    height: 1000px;
    overflow: hidden;
    background: var(--page);
  }
  .canvas {
    position: relative;
    width: 1200px;
    height: 1000px;
  }
  .label {
    position: absolute;
    left: 408px;
    top: 116px;
    width: 384px;
    height: 768px;
    background: var(--paper);
  }
  .label-frame {
    position: absolute;
    left: 12px;
    top: 14px;
    right: 12px;
    bottom: 14px;
    border: 3px solid var(--ink);
  }
  .seal {
    position: absolute;
    left: 0;
    top: 0;
  }
  .seal text {
    font-family: "Tenor Sans", sans-serif;
    fill: var(--ink);
  }
  .seal-arc-text {
    font-size: 21px;
    letter-spacing: 5px;
  }
  .seal-brand {
    font-size: 30px;
    letter-spacing: 4px;
  }
  .bee-illustration {
    position: absolute;
    left: 102px;
    top: 370px;
    width: 180px;
    height: 165px;
    background: radial-gradient(ellipse at center, var(--bee-tone) 0%, rgba(185,178,166,0.35) 55%, rgba(246,239,227,0) 75%);
  }
  .product-name {
    position: absolute;
    left: 0;
    right: 0;
    top: 550px;
    text-align: center;
    font-family: "Tenor Sans", sans-serif;
    color: var(--ink);
  }
  .product-kicker {
    display: flex;
    align-items: center;
    justify-content: center;
    gap: 12px;
    font-size: 27px;
    letter-spacing: 5px;
    line-height: 34px;
  }
  .product-kicker::before,
  .product-kicker::after {
    content: "";
    display: block;
    width: 46px;
    height: 3px;
    background: var(--ink);
  }
  .product-line {
    font-size: 54px;
    letter-spacing: 5px;
    line-height: 66px;
  }
</style>
</head>
<body>
<div class="canvas">
  <div class="label">
    <div class="label-frame"></div>

    <svg class="seal" width="384" height="360" viewBox="0 0 384 360" aria-label="Corrow Family Farms, Pinebrook, USA">
      <defs>
        <path id="seal-top-arc" d="M 52 222 A 140 140 0 0 1 332 222"/>
        <path id="seal-bottom-arc" d="M 77 222 A 115 115 0 0 0 307 222"/>
      </defs>
      <text class="seal-arc-text">
        <textPath href="#seal-top-arc" startOffset="50%" text-anchor="middle">CORROW FAMILY FARMS</textPath>
      </text>
      <text class="seal-arc-text">
        <textPath href="#seal-bottom-arc" startOffset="50%" text-anchor="middle">PINEBROOK, USA</textPath>
      </text>
      <circle cx="54" cy="222" r="4.5" fill="var(--ink)"/>
      <circle cx="331" cy="222" r="4.5" fill="var(--ink)"/>
      <text class="seal-brand" x="192" y="232" text-anchor="middle">CORROW</text>
    </svg>

    <div class="bee-illustration" role="img" aria-label="Vintage engraved illustration of a honey bee with spread wings"></div>

    <div class="product-name">
      <div class="product-kicker">FARM</div>
      <div class="product-line">FRESH</div>
      <div class="product-line">HONEY</div>
    </div>
  </div>
</div>
</body>
</html>
```